Need Letterhead and Business Card

I have a logo but i need new letterhead and biz cards. We are a real estate investment firm so we need very professional but also do not want to be old fashioned. We have 3 locations; Singapore, New York and Ponte Vedra Florida. I can provide full addresses if needed. If you have adjustments to our logo you would recommend we are open to them.
I will be putting in a separate project but we also need a template for our own powerpoint slide presentations and website.

Industry/Entity Type

Real Estate

```html
<!DOCTYPE html>
<html lang="en">
<head>
<meta charset="utf-8">
<title>Alden Letterhead</title>
<link href="https://fonts.googleapis.com/css2?family=Mulish:wght@400;600;700;800&display=swap" rel="stylesheet">
<style>
  :root {
    --backdrop: #a9c3df;
    --paper: #eeeeef;
    --paper-mark: #e5e5e8;
    --navy: #1f3a78;
    --gold: #c99a3a;
    --ink: #55585e;
    --ink-soft: #6b6e74;
    --signature-tone: #d9d9dc;
  }
  * { box-sizing: border-box; margin: 0; padding: 0; }
  html, body { width: 1200px; height: 1000px; overflow: hidden; }
  body {
    background: var(--backdrop);
    font-family: "Mulish", Arial, sans-serif;
    position: relative;
  }
  .letterhead {
    position: absolute;
    top: 190px;
    width: 390px;
    height: 560px;
    background: var(--paper);
    overflow: hidden;
  }
  .letterhead--first { left: 163px; }
  .letterhead--second { left: 653px; }

  .page-mark {
    position: absolute;
    border-radius: 50%;
    background: var(--paper-mark);
  }
  .letterhead--first .page-mark { left: 300px; top: 140px; width: 130px; height: 130px; }
  .letterhead--second .page-mark { left: 60px; top: 430px; width: 150px; height: 150px; }

  .brand {
    position: absolute;
    left: 47px;
    top: 33px;
    width: 92px;
  }
  .brand__name {
    display: block;
    color: var(--navy);
    font-weight: 800;
    font-size: 25px;
    line-height: 30px;
    letter-spacing: 0.3px;
  }
  .brand__tagline {
    display: block;
    margin-top: 3px;
    padding-top: 2px;
    border-top: 1px solid var(--navy);
    color: var(--gold);
    font-size: 4.1px;
    font-weight: 600;
    letter-spacing: 0.2px;
    text-transform: uppercase;
    white-space: nowrap;
  }

  .offices {
    position: absolute;
    left: 183px;
    top: 49px;
    display: flex;
    gap: 15px;
  }
  .office { width: 42px; }
  .office__city {
    color: var(--gold);
    font-size: 6.5px;
    font-weight: 700;
    line-height: 9px;
  }
  .office__address {
    color: var(--ink);
    font-size: 4.2px;
    line-height: 6px;
    white-space: nowrap;
  }

  .letter {
    position: absolute;
    left: 52px;
    top: 144px;
    width: 288px;
    color: var(--ink);
    font-size: 6.8px;
    line-height: 10.9px;
  }
  .letter__greeting { margin-bottom: 8px; }
  .letter__paragraph {
    text-align: justify;
    margin-bottom: 10.9px;
  }
  .letter__signature {
    display: block;
    margin: 38px 0 0 34px;
    width: 92px;
    height: 22px;
    background: var(--signature-tone);
  }

  .contact-bar {
    position: absolute;
    left: 78px;
    top: 537px;
    display: flex;
    align-items: center;
    font-size: 5.2px;
    color: var(--ink);
    white-space: nowrap;
  }
  .contact-bar__item b { color: var(--navy); font-weight: 700; }
  .contact-bar__divider {
    width: 1px;
    height: 7px;
    background: var(--ink-soft);
    margin: 0 10px;
  }
</style>
</head>
<body>

<article class="letterhead letterhead--first">
  <div class="page-mark" role="img" aria-label="Faint brand watermark"></div>
  <header>
    <div class="brand">
      <span class="brand__name">ALDEN</span>
      <span class="brand__tagline">Real Estate Investment &amp; Management</span>
    </div>
    <div class="offices">
      <div class="office">
        <p class="office__city">Singapore</p>
        <p class="office__address">123, Main Fake Street,<br>Anytown, Postal Code.</p>
      </div>
      <div class="office">
        <p class="office__city">New York</p>
        <p class="office__address">123, Main Fake Street,<br>Anytown, Postal Code.</p>
      </div>
      <div class="office">
        <p class="office__city">Florida</p>
        <p class="office__address">123, Main Fake Street,<br>Anytown, Postal Code.</p>
      </div>
    </div>
  </header>
  <section class="letter">
    <p class="letter__greeting">Dear Client,</p>
    <p class="letter__paragraph">Lorem ipsum dolor sit amet, consectetur adipiscing elit. Nulla sodales nisi vitae Lorem ipsum dolor sit amet, consectetur adipiscing elit. Suspendisse feugiat eros nisl, a facilisis risus eleifend sed. Aliquam mauris enim, fermentum eu lacinia sit amet, laoreet eu leo. Nullam eleifend nulla in libero tristique, ac vulputate odio tincidunt. Etiam non condimentum tortor. Integer suscipit neque nec odio porttitor cursus. Phasellus a sapien blandit, suscipit justo id, condimentum ante. Morbi tristique justo risus, id mattis dui molestie ut. Nullam volutpat ut quam commodo faucibus. Pellentesque urna est, interdum in elit quis, pharetra elementum orci. Nam pharetra velit molestie justo placerat scelerisque.</p>
    <p class="letter__paragraph">Sed est tellus, rutrum in nisl a, consequat sollicitudin elit. Aliquam vitae vestibulum felis. Morbi iaculis nunc volutpat diam ullamcorper vestibulum. Nulla facilisi. Aenean accumsan gravida orci, vitae consectetur justo aliquet et. Curabitur vehicula tempus dolor, a gravida metus vestibulum sit amet. Integer non erat elementum, malesuada metus vel, fermentum lectus. Etiam sit amet nisl ac augue semper ultrices.</p>
    <p class="letter__paragraph">Nulla tincidunt molestie libero vel pretium. Donec condimentum nulla sit amet risus semper imperdiet. Duis congue eros nec diam blandit, et pellentesque sapien auctor.</p>
    <p class="letter__closing">Best regards,</p>
    <span class="letter__signature" role="img" aria-label="Handwritten signature of Daniel Hart"></span>
  </section>
  <footer class="contact-bar">
    <span class="contact-bar__item"><b>Phone:</b> 555-0192-4410</span>
    <span class="contact-bar__divider"></span>
    <span class="contact-bar__item"><b>Fax:</b> 555-0192-4411</span>
    <span class="contact-bar__divider"></span>
    <span class="contact-bar__item"><b>E-mail:</b> contact@alden.sg</span>
    <span class="contact-bar__divider"></span>
    <span class="contact-bar__item"><b>Web:</b> www.alden.sg</span>
  </footer>
</article>

<article class="letterhead letterhead--second">
  <div class="page-mark" role="img" aria-label="Faint brand watermark"></div>
  <header>
    <div class="brand">
      <span class="brand__name">ALDEN</span>
      <span class="brand__tagline">Real Estate Investment &amp; Management</span>
    </div>
    <div class="offices">
      <div class="office">
        <p class="office__city">Singapore</p>
        <p class="office__address">123, Main Fake Street,<br>Anytown, Postal Code.</p>
      </div>
      <div class="office">
        <p class="office__city">New York</p>
        <p class="office__address">123, Main Fake Street,<br>Anytown, Postal Code.</p>
      </div>
      <div class="office">
        <p class="office__city">Florida</p>
        <p class="office__address">123, Main Fake Street,<br>Anytown, Postal Code.</p>
      </div>
    </div>
  </header>
  <section class="letter">
    <p class="letter__greeting">Dear Client,</p>
    <p class="letter__paragraph">Lorem ipsum dolor sit amet, consectetur adipiscing elit. Nulla sodales nisi vitae Lorem ipsum dolor sit amet, consectetur adipiscing elit. Suspendisse feugiat eros nisl, a facilisis risus eleifend sed. Aliquam mauris enim, fermentum eu lacinia sit amet, laoreet eu leo. Nullam eleifend nulla in libero tristique, ac vulputate odio tincidunt. Etiam non condimentum tortor. Integer suscipit neque nec odio porttitor cursus. Phasellus a sapien blandit, suscipit justo id, condimentum ante. Morbi tristique justo risus, id mattis dui molestie ut. Nullam volutpat ut quam commodo faucibus. Pellentesque urna est, interdum in elit quis, pharetra elementum orci. Nam pharetra velit molestie justo placerat scelerisque.</p>
    <p class="letter__paragraph">Sed est tellus, rutrum in nisl a, consequat sollicitudin elit. Aliquam vitae vestibulum felis. Morbi iaculis nunc volutpat diam ullamcorper vestibulum. Nulla facilisi. Aenean accumsan gravida orci, vitae consectetur justo aliquet et. Curabitur vehicula tempus dolor, a gravida metus vestibulum sit amet. Integer non erat elementum, malesuada metus vel, fermentum lectus. Etiam sit amet nisl ac augue semper ultrices.</p>
    <p class="letter__paragraph">Nulla tincidunt molestie libero vel pretium. Donec condimentum nulla sit amet risus semper imperdiet. Duis congue eros nec diam blandit, et pellentesque sapien auctor.</p>
    <p class="letter__closing">Best regards,</p>
    <span class="letter__signature" role="img" aria-label="Handwritten signature of Daniel Hart"></span>
  </section>
  <footer class="contact-bar">
    <span class="contact-bar__item"><b>Phone:</b> 555-0192-4410</span>
    <span class="contact-bar__divider"></span>
    <span class="contact-bar__item"><b>Fax:</b> 555-0192-4411</span>
    <span class="contact-bar__divider"></span>
    <span class="contact-bar__item"><b>E-mail:</b> contact@alden.sg</span>
    <span class="contact-bar__divider"></span>
    <span class="contact-bar__item"><b>Web:</b> www.alden.sg</span>
  </footer>
</article>

</body>
</html>
```